We are looking to design a black on white bourbon label for a new brand
in att we have added
1. the bottle we need to use (wine bottle in black)
2. some industry examples (Look at horse rider label good example of where we need to go)
3. horses and cowboys illistrations

The brand will be Called MARROWGATE RUN. we want an old school feeling label prohibition style.

What we need on the label is
1. visual = Bucking Horse + rider cowboy + lasso forming a circle
2. Name = Marrowgate Run Bourbon Straight Aged Whiskey
3. Product info = 70 CL 40 ABV
4. Distilled in the Wild Wild West WWW.MARROWGATERUNWHISKEY.EXAMPLE

```html
<!DOCTYPE html>
<html lang="en">
<head>
<meta charset="utf-8">
<title>Marrowgate Run Bourbon – Label</title>
<link rel="stylesheet" href="https://fonts.googleapis.com/css2?family=Oswald:wght@300;400&family=Old+Standard+TT:wght@400;700&family=Rye&family=Tinos:wght@700&display=swap">
<style>
  :root {
    --page: #ffffff;
    --label-dark: #1b1c1d;
    --label-mid: #2a2b2d;
    --gold: #c9a36a;
    --gold-soft: #a88757;
    --hatch: #8a8b8d;
    --ink-white: #ecebe8;
    --bourbon-red: #d5262b;
    --whiskey-yellow: #e4cf2a;
    --url-yellow: #d8c12c;
  }
  * { margin: 0; padding: 0; box-sizing: border-box; }
  html, body {
    width: 1200px;
    height: 1029px;
    overflow: hidden;
    background: var(--page);
  }
  .canvas {
    position: relative;
    width: 1200px;
    height: 1029px;
  }
  .label {
    position: absolute;
    left: 335px;
    top: 35px;
    width: 530px;
    height: 960px;
    background: radial-gradient(ellipse at 50% 45%, var(--label-mid), var(--label-dark) 75%);
    color: var(--ink-white);
  }
  .label-frame {
    position: absolute;
    inset: 0;
    width: 530px;
    height: 960px;
  }
  .label-illustration {
    position: absolute;
    left: 46px;
    top: 108px;
    width: 430px;
    height: 492px;
    border-radius: 50% 50% 30% 30%;
    background: radial-gradient(ellipse at 40% 60%, rgba(220,220,220,0.16), rgba(120,120,120,0.06) 55%, rgba(0,0,0,0) 75%);
  }
  .brand-name {
    position: absolute;
    left: 203px;
    top: 188px;
    width: 240px;
    text-align: center;
    font-family: "Oswald", sans-serif;
    font-weight: 300;
    font-size: 29px;
    letter-spacing: 0.5px;
    color: var(--ink-white);
    line-height: 1;
  }
  .product-type {
    position: absolute;
    left: 193px;
    top: 236px;
    width: 260px;
    text-align: center;
    font-family: "Old Standard TT", serif;
    font-weight: 400;
    font-size: 60px;
    line-height: 1;
    color: var(--bourbon-red);
    transform: scaleX(0.82);
  }
  .straight-aged {
    position: absolute;
    left: 250px;
    top: 562px;
    width: 200px;
    text-align: center;
    font-family: "Rye", serif;
    font-size: 27px;
    line-height: 1;
    color: var(--ink-white);
  }
  .rule {
    position: absolute;
    left: 84px;
    width: 362px;
    height: 5px;
    border-top: 2px solid var(--gold);
    border-bottom: 1px solid var(--gold-soft);
  }
  .rule--top { top: 600px; }
  .rule--bottom { top: 709px; }
  .whiskey {
    position: absolute;
    left: 70px;
    top: 612px;
    width: 390px;
    text-align: center;
    font-family: "Rye", serif;
    font-size: 74px;
    line-height: 1.1;
    color: var(--whiskey-yellow);
  }
  .spec {
    position: absolute;
    top: 733px;
    width: 54px;
    height: 54px;
    border: 2px solid var(--ink-white);
    border-radius: 50%;
    display: flex;
    flex-direction: column;
    align-items: center;
    justify-content: center;
    font-family: "Oswald", sans-serif;
    font-weight: 400;
    line-height: 1;
  }
  .spec--abv { left: 68px; }
  .spec--volume { left: 406px; }
  .spec-value { font-size: 20px; }
  .spec-unit { font-size: 12px; margin-top: 2px; }
  .origin {
    position: absolute;
    left: 125px;
    top: 742px;
    width: 280px;
    text-align: center;
    font-family: "Tinos", serif;
    font-weight: 700;
    font-size: 17px;
    line-height: 1;
    color: var(--ink-white);
  }
  .website {
    position: absolute;
    left: 115px;
    top: 772px;
    width: 300px;
    text-align: center;
    font-family: "Oswald", sans-serif;
    font-weight: 400;
    font-size: 16px;
    line-height: 1;
    color: var(--url-yellow);
    transform: scaleX(0.8);
  }
</style>
</head>
<body>
<div class="canvas">
  <div class="label">
    <svg class="label-frame" viewBox="0 0 530 960" aria-hidden="true">
      <path d="M70 23 H460 V40 H498 V80 H515 V880 H498 V920 H460 V937 H70 V920 H32 V880 H20 V80 H32 V40 H70 Z"
            fill="none" stroke="var(--hatch)" stroke-width="6" stroke-dasharray="1.5 2"/>
      <path d="M78 36 H452 V52 H486 V88 H500 V872 H486 V908 H452 V924 H78 V908 H44 V872 H32 V88 H44 V52 H78 Z"
            fill="none" stroke="var(--gold)" stroke-width="2"/>
      <path d="M84 44 H446 V60 H478 V94 H492 V866 H478 V900 H446 V916 H84 V900 H52 V866 H40 V94 H52 V60 H84 Z"
            fill="none" stroke="var(--gold-soft)" stroke-width="1"/>
    </svg>

    <div class="label-illustration" role="img" aria-label="Illustration of a cowboy on a bucking horse swinging a lasso that forms a large circle"></div>

    <div class="brand-name">MARROWGATE RUN</div>
    <div class="product-type">BOURBON</div>

    <div class="straight-aged">Straight Aged</div>
    <div class="rule rule--top"></div>
    <div class="whiskey">WHISKEY</div>
    <div class="rule rule--bottom"></div>

    <div class="spec spec--abv"><span class="spec-value">40</span><span class="spec-unit">ABV</span></div>
    <div class="origin">Distilled in the Wild Wild West</div>
    <div class="website">WWW.MARROWGATERUNWHISKEY.EXAMPLE</div>
    <div class="spec spec--volume"><span class="spec-value">70</span><span class="spec-unit">CL</span></div>
  </div>
</div>
</body>
</html>
```